Business card

We need a business card design for our company based in Auckland , New Zealand called 'Kestrel + Design Ltd'. We provide architectural services. We would like to see designs that use the max. three colours (such as white, black, grey) The final design should communicate financial safety and growth."
Also I will provide our company logo. I would like to the logo to be embeded onto our business card.

Target Market(s)

new residential house, alteration & addition & light commericila design & drafting service

Industry/Entity Type

Architecture

Contact Information for Business Card

Company name: kestrel + design Ltd.
Name: Mark Telford
Job title: architectural designer & Design RQC
email address: mark@kdstudio.co.nz
mobile number: 02 5319 6620
web site: www.kdstudio.co.nz

Requirements
Must have
• My project must have..
• - embeded logo (attached company logo)
• I don't have a bigger version for our company logo, but I have one old one, so you can remove the word from it)
• - insert the attached small PDGQ logo & RQC logo
• - creative, simple and clear business card.
• - Max. three colours
Nice to have
• - Here are the samples I would like to share with you: http://www.velmorindex.com/blog/minimalistic-business-card-designs/
• I would like to have my business card like one of the creation.
Should not have
• TBA

```html
<!DOCTYPE html>
<html lang="en">
<head>
<meta charset="utf-8">
<title>Kestrel + Design Ltd – Business Card</title>
<link href="https://fonts.googleapis.com/css2?family=Open+Sans:wght@400;600;700&display=swap" rel="stylesheet">
<style>
  :root {
    --page: #ffffff;
    --card-light: #ffffff;
    --card-dark: #0b0b0b;
    --ink: #1a1a1a;
    --grey: #8a8a80;
    --rule: #333333;
    --white: #ffffff;
  }
  html, body {
    margin: 0;
    padding: 0;
    width: 1200px;
    height: 1200px;
    overflow: hidden;
    background: var(--page);
    font-family: "Open Sans", Arial, sans-serif;
  }
  .canvas {
    position: relative;
    width: 1200px;
    height: 1200px;
  }
  .card {
    position: absolute;
    left: 183px;
    width: 834px;
    height: 497px;
    box-shadow: 8px 10px 10px rgba(0,0,0,0.45);
  }
  .card-front {
    top: 57px;
    background: var(--card-light);
    border: 1px solid #e4e4e4;
    box-sizing: border-box;
  }
  .card-back {
    top: 631px;
    background: var(--card-dark);
    color: var(--white);
  }
  .brand-mark {
    position: absolute;
    left: 331px;
    top: 136px;
    width: 172px;
    height: 172px;
  }
  .company-name {
    position: absolute;
    left: 0;
    right: 0;
    top: 364px;
    margin: 0;
    text-align: center;
    font-size: 38px;
    font-weight: 600;
    color: var(--ink);
    letter-spacing: 0.2px;
  }
  .membership {
    position: absolute;
    left: 122px;
    top: 48px;
    color: var(--grey);
    font-weight: 700;
  }
  .membership-name {
    display: block;
    font-size: 50px;
    line-height: 1;
    letter-spacing: -1px;
  }
  .membership-level {
    display: block;
    margin-top: 18px;
    font-size: 21px;
    line-height: 1.05;
  }
  .practitioner-badge {
    position: absolute;
    left: 531px;
    top: 24px;
    width: 178px;
    height: 178px;
  }
  .divider {
    position: absolute;
    left: 103px;
    width: 625px;
    top: 242px;
    height: 1px;
    background: var(--rule);
  }
  .person {
    position: absolute;
    left: 122px;
    top: 293px;
  }
  .person-name {
    margin: 0;
    font-size: 28px;
    font-weight: 400;
    line-height: 1.1;
  }
  .person-title {
    margin: 4px 0 0;
    font-size: 17px;
    line-height: 1.3;
  }
  .contact-list {
    position: absolute;
    left: 122px;
    top: 382px;
    margin: 0;
    display: grid;
    grid-template-columns: 115px auto;
    row-gap: 4px;
    font-size: 16px;
    line-height: 23px;
  }
  .contact-list dt, .contact-list dd { margin: 0; }
</style>
</head>
<body>
<main class="canvas">
  <section class="card card-front" aria-label="Card front">
    <svg class="brand-mark" viewBox="0 0 172 172" aria-hidden="true">
      <circle cx="86" cy="86" r="76" fill="none" stroke="var(--ink)" stroke-width="14"/>
    </svg>
    <h1 class="company-name">Kestrel + Design Ltd</h1>
  </section>

  <section class="card card-back" aria-label="Card back">
    <div class="membership">
      <span class="membership-name">PDGQ</span>
      <span class="membership-level">Professional<br>Member</span>
    </div>
    <svg class="practitioner-badge" viewBox="0 0 178 178" aria-label="Practitioner badge" role="img">
      <circle cx="89" cy="89" r="87" fill="var(--white)"/>
      <circle cx="89" cy="89" r="62" fill="var(--card-dark)"/>
    </svg>
    <div class="divider"></div>
    <div class="person">
      <h2 class="person-name">Mark Telford</h2>
      <p class="person-title">Architectural Designer &amp; Design RQC</p>
    </div>
    <dl class="contact-list">
      <dt>T</dt><dd>02 5319 6620</dd>
      <dt>M</dt><dd>mark@kdstudio.co.nz</dd>
      <dt>W</dt><dd>www.kdstudio.co.nz</dd>
    </dl>
  </section>
</main>
</body>
</html>
```